Small Business Consulting Firm Needs Business Card Design

Need a sleek modern business card with 2 sides matching the colors of our logo. We will be placing these with a mailer we are sending out. These business cards will only ever be given to business owners. We operate helping businesses who are struggling with cash flow or finances. If the green and blue design needs to be moved to the right of "Harborline Crest Consulting" for aesthetic purposes that is ok. We will need an editable file if possible. We would like to include the reps name, email, website, and phone number. For now just use Peter Vance, pvance@harborlinecrest.com, www.harborlinecrest.com, and 833-555-0172.

```html
<!DOCTYPE html>
<html lang="en">
<head>
<meta charset="UTF-8">
<title>Harborline Crest Consulting — Business Card Back</title>
<link href="https://fonts.googleapis.com/css2?family=Montserrat:wght@400&display=swap" rel="stylesheet">
<style>
  :root {
    --card-black: #030607;
    --brand-green: #7aba43;
    --text-white: #ffffff;
  }
  html, body {
    margin: 0;
    padding: 0;
    width: 668px;
    height: 1200px;
    overflow: hidden;
    background: var(--card-black);
  }
  .card {
    position: relative;
    width: 668px;
    height: 1200px;
    background: var(--card-black);
    color: var(--text-white);
    font-family: "Montserrat", sans-serif;
    font-weight: 400;
  }
  .brand-square {
    position: absolute;
    left: 289px;
    top: 503px;
    width: 90px;
    height: 90px;
    background: var(--brand-green);
  }
  .brand-name {
    position: absolute;
    left: 0;
    width: 668px;
    text-align: center;
    margin: 0;
    font-weight: 400;
    color: var(--text-white);
  }
  .brand-name__main {
    top: 656px;
    font-size: 41px;
    letter-spacing: 0.04em;
    line-height: 1;
  }
  .brand-name__sub {
    top: 714px;
    font-size: 24px;
    letter-spacing: 0.8em;
    padding-left: 0.8em;
    box-sizing: border-box;
    line-height: 1;
  }
  .website {
    position: absolute;
    left: 0;
    top: 1072px;
    width: 668px;
    text-align: center;
    font-size: 29px;
    line-height: 1;
    color: var(--text-white);
  }
</style>
</head>
<body>
  <main class="card">
    <div class="brand-square" aria-hidden="true"></div>
    <p class="brand-name brand-name__main">HARBORLINE CREST</p>
    <p class="brand-name brand-name__sub">CONSULTING</p>
    <div class="website">www.harborlinecrest.com</div>
  </main>
</body>
</html>
```